KV Media Group stationary project
don't have one
Use same font as used in my logo
logo attached
Molly Brennan
President/CEO
don't have one yet
mbrennan@kvmediagroupexample.com
www.kvmediagroupexample.com
I don't have an address yet so can you do an A & B version so I know what it will look like and can add the address at a later date. Also, as part of this contest which includes business card/letterhead/envelopes, can you also do a design for invoice and fax sheet. Thanks!

```html
<!DOCTYPE html>
<html lang="en">
<head>
<meta charset="utf-8">
<title>KV Media Group Stationery</title>
<link href="https://fonts.googleapis.com/css2?family=Exo+2:wght@700&family=Open+Sans:wght@400;600&display=swap" rel="stylesheet">
<style>
:root{
  --board:#3b3b3b;
  --board-dark:#2f2f2f;
  --paper:#ffffff;
  --orange:#f6a400;
  --orange-light:#fcc419;
  --ink:#1d1d1d;
  --label:#c9c9c9;
  --mute:#8a8a8a;
  --watermark:#ededed;
}
*{box-sizing:border-box;margin:0;padding:0}
html,body{width:1200px;height:451px;overflow:hidden}
body{background:radial-gradient(circle at 50% 40%,var(--board),var(--board-dark));font-family:"Open Sans",sans-serif;position:relative}
.piece{position:absolute;background:var(--paper);overflow:hidden;box-shadow:0 2px 6px rgba(0,0,0,.45)}
.piece svg.art{position:absolute;inset:0;width:100%;height:100%}
.label{position:absolute;color:var(--label);font-size:7px;text-align:center}
.brand{position:absolute;display:flex;align-items:center;gap:4px;font-family:"Exo 2",sans-serif;font-weight:700;color:var(--ink);white-space:nowrap}
.brand .dot{border-radius:50%;background:var(--orange);flex:none}
.brand.on-orange{color:var(--ink)}
.brand.on-orange .dot{background:var(--ink)}
.mark-faint{position:absolute;border-radius:50%;border:10px solid var(--watermark);display:flex;align-items:center;justify-content:center;font-family:"Exo 2",sans-serif;font-weight:700;color:var(--watermark);text-align:center}
.small{position:absolute;font-size:5px;line-height:1.5;color:var(--mute)}
.orange-fill{background:linear-gradient(135deg,var(--orange-light),var(--orange))}

/* business cards */
.card-front{left:24px;top:36px;width:168px;height:100px}
.card-back-a{left:24px;top:180px;width:168px;height:100px}
.card-back-b{left:24px;top:306px;width:168px;height:96px}
.person{position:absolute;right:6px;top:10px;text-align:right;color:var(--paper);font-size:5px;line-height:1.5;white-space:nowrap}
.person strong{font-weight:600;font-size:6.5px}

/* letterheads */
.letterhead-a{left:216px;top:29px;width:283px;height:384px}
.letterhead-b{left:528px;top:29px;width:283px;height:384px}

/* envelopes */
.envelope-back{left:838px;top:29px;width:338px;height:144px}
.envelope-flap{left:838px;top:178px;width:338px;height:122px}
.envelope-front{left:838px;top:320px;width:338px;height:94px}
</style>
</head>
<body>

<!-- Front card -->
<section class="piece card-front">
  <svg class="art" viewBox="0 0 168 100" preserveAspectRatio="none">
    <path d="M58 0H168V100H132C96 80 62 50 58 0Z" fill="#f6a400"/>
    <path d="M53 0C57 52 92 81 127 100" stroke="#1d1d1d" stroke-width="1.5" fill="none"/>
  </svg>
  <div class="person"><strong>Molly Brennan</strong><br>President/CEO<br>mbrennan@kvmediagroupexample.com<br>www.kvmediagroupexample.com</div>
  <div class="brand" style="left:8px;top:78px;font-size:8.5px"><span class="dot" style="width:10px;height:10px"></span>KV Media Group</div>
</section>
<div class="label" style="left:24px;top:142px;width:168px">Front Card</div>

<!-- Back card A -->
<section class="piece card-back-a">
  <svg class="art" viewBox="0 0 168 100" preserveAspectRatio="none">
    <path d="M0 82C50 72 110 74 168 86V100H0Z" fill="#f6a400"/>
    <path d="M0 80C50 70 110 72 168 84" stroke="#1d1d1d" stroke-width="1.5" fill="none"/>
  </svg>
  <div class="brand" style="left:22px;top:34px;font-size:14px"><span class="dot" style="width:16px;height:16px"></span>KV Media Group</div>
</section>
<div class="label" style="left:24px;top:286px;width:168px">Back Card Option A</div>

<!-- Back card B -->
<section class="piece card-back-b orange-fill">
  <div class="brand on-orange" style="left:22px;top:38px;font-size:14px"><span class="dot" style="width:16px;height:16px"></span>KV Media Group</div>
</section>
<div class="label" style="left:24px;top:414px;width:168px">Back Card Option B</div>

<!-- Letterhead A -->
<section class="piece letterhead-a">
  <svg class="art" viewBox="0 0 283 384" preserveAspectRatio="none">
    <path d="M0 0H18C30 120 10 260 22 384H0Z" fill="#f6a400"/>
    <path d="M22 0C34 120 14 260 26 384" stroke="#1d1d1d" stroke-width="1.5" fill="none"/>
  </svg>
  <div class="brand" style="left:34px;top:14px;font-size:10px"><span class="dot" style="width:14px;height:14px"></span>KV Media Group</div>
  <div class="small" style="left:150px;top:14px">Street Address Line<br>City, State Zip<br>mbrennan@kvmediagroupexample.com<br>www.kvmediagroupexample.com</div>
  <div class="mark-faint" style="left:86px;top:136px;width:112px;height:112px;font-size:13px">KV Media Group</div>
</section>
<div class="label" style="left:216px;top:420px;width:283px">Letterhead Option A</div>

<!-- Letterhead B -->
<section class="piece letterhead-b">
  <svg class="art" viewBox="0 0 283 384" preserveAspectRatio="none">
    <path d="M0 350C90 338 190 338 283 352V384H0Z" fill="#f6a400"/>
    <path d="M0 346C90 334 190 334 283 348" stroke="#1d1d1d" stroke-width="1.5" fill="none"/>
  </svg>
  <div class="mark-faint" style="left:86px;top:120px;width:112px;height:112px;font-size:13px">KV Media Group</div>
  <div class="small" style="left:0;width:283px;top:320px;text-align:center">Street Address Line · City, State Zip<br>mbrennan@kvmediagroupexample.com · www.kvmediagroupexample.com</div>
</section>
<div class="label" style="left:528px;top:420px;width:283px">Letterhead Option B</div>

<!-- Envelope back -->
<section class="piece envelope-back">
  <svg class="art" viewBox="0 0 338 144" preserveAspectRatio="none">
    <path d="M0 0H338V70C240 92 110 92 0 70Z" fill="#f6a400"/>
    <path d="M0 74C110 96 240 96 338 74" stroke="#1d1d1d" stroke-width="1.5" fill="none"/>
  </svg>
  <div class="brand on-orange" style="left:210px;top:18px;font-size:11px"><span class="dot" style="width:16px;height:16px"></span>KV Media Group</div>
  <div class="small" style="left:0;width:338px;top:110px;text-align:center">www.kvmediagroupexample.com</div>
</section>

<!-- Envelope flap -->
<section class="piece envelope-flap">
  <svg class="art" viewBox="0 0 338 122" preserveAspectRatio="none">
    <path d="M0 0L169 66L338 0" stroke="#d4d4d4" stroke-width="1" fill="none"/>
    <path d="M0 122L140 58M338 122L198 58" stroke="#e2e2e2" stroke-width="1" fill="none"/>
  </svg>
  <div class="small" style="left:0;width:338px;top:18px;text-align:center">www.kvmediagroupexample.com</div>
</section>
<div class="label" style="left:838px;top:305px;width:338px">Envelope Back</div>

<!-- Envelope front -->
<section class="piece envelope-front">
  <svg class="art" viewBox="0 0 338 94" preserveAspectRatio="none">
    <path d="M0 70C120 60 230 62 338 76V94H0Z" fill="#f6a400"/>
    <path d="M0 66C120 56 230 58 338 72" stroke="#1d1d1d" stroke-width="1.5" fill="none"/>
  </svg>
  <div class="brand" style="left:12px;top:10px;font-size:9px"><span class="dot" style="width:11px;height:11px"></span>KV Media Group</div>
  <div class="small" style="left:12px;top:26px">Street Address Line<br>City, State Zip</div>
</section>
<div class="label" style="left:838px;top:420px;width:338px">Envelope Front</div>

</body>
</html>
```